Design a PowerPoint template for a consultancy organisation

I am after a Powerpoint template including three pages a title slide (that should have a title and subtitle), A title and content slide and a section header slide. I expect the company name and/or logo to be prominent and the colors to work well with the logo colors. I have included a copy of the logo

```html
<!DOCTYPE html>
<html lang="en">
<head>
<meta charset="utf-8">
<title>Quorvane – Presentation Template</title>
<link href="https://fonts.googleapis.com/css2?family=Montserrat:wght@300;400;500;600;700;800&display=swap" rel="stylesheet">
<style>
:root{
  --green:#8cc63f;
  --purple:#6a1bb3;
  --ink:#1d1d1d;
  --text:#333333;
  --backdrop:#a3a3a3;
  --white:#ffffff;
  --rule:#e6e6e6;
}
*{margin:0;padding:0;box-sizing:border-box}
html,body{width:1200px;height:685px;overflow:hidden;background:var(--backdrop);font-family:'Montserrat',sans-serif}
.canvas{position:relative;width:1200px;height:685px}
.slide{position:absolute;width:589px;height:331px;background:var(--white);overflow:hidden}
.slide--title{left:8px;top:8px}
.slide--cover{left:603px;top:8px}
.slide--content{left:8px;top:346px}
.slide--section{left:603px;top:346px}

.brand{position:absolute;display:flex;align-items:center;gap:5px;color:var(--green);font-weight:600;white-space:nowrap;line-height:1}
.brand__mark{background:var(--purple);flex:none}
.brand--lg{font-size:19px}
.brand--lg .brand__mark{width:13px;height:13px}
.brand--sm{font-size:11px}
.brand--sm .brand__mark{width:8px;height:8px}

/* title slide */
.slide--title .bar-top{position:absolute;left:0;top:0;width:100%;height:4px;background:var(--green)}
.slide--title .bar-bottom{position:absolute;left:0;bottom:0;width:100%;height:4px;background:var(--purple)}
.slide--title .brand{left:30px;top:103px}
.headline{position:absolute;left:29px;top:146px;color:var(--ink);line-height:1}
.headline__main{font-size:36px;font-weight:800;letter-spacing:-.3px}
.headline__sub{font-size:26px;font-weight:700;margin-top:3px}
.headline__tagline{font-size:17px;font-weight:600;color:var(--purple);margin-top:3px}
.pill{position:absolute;background:var(--green);color:var(--white);border-radius:12px;display:flex;align-items:center;justify-content:center}
.pill--presenter{left:32px;top:266px;width:98px;height:23px;font-size:9.5px;font-weight:400}

/* cover slide */
.cover-photo{position:absolute;left:0;top:0;width:100%;height:258px;background:linear-gradient(135deg,#7a2bd0 0%,#6a1bb3 50%,#5410a0 100%)}
.cover-text{position:absolute;left:0;top:0;width:100%;height:258px;text-align:center;color:var(--white)}
.cover-url{position:absolute;left:182px;top:66px;width:210px;height:17px;border-radius:9px;background:rgba(120,50,200,.8);font-size:8.5px;letter-spacing:2.6px;display:flex;align-items:center;justify-content:center}
.cover-title{position:absolute;left:0;top:97px;width:100%;font-size:39px;font-weight:800;line-height:1}
.cover-subtitle{position:absolute;left:0;top:138px;width:100%;font-size:32px;font-weight:300;line-height:1}
.cover-tagline{position:absolute;left:0;top:177px;width:100%;font-size:16px;font-weight:400;letter-spacing:2.2px;color:var(--green)}
.pill--date{left:403px;top:246px;width:150px;height:26px;font-size:10px;font-weight:700;border-radius:13px}
.slide--cover .brand{left:28px;top:300px}

/* shared footer */
.footer{position:absolute;left:0;bottom:0;width:100%;height:21px;background:var(--green)}
.footer__copy{position:absolute;left:14px;top:8px;font-size:4.8px;letter-spacing:1.8px;color:var(--white);font-weight:600}
.footer__page{position:absolute;right:0;top:0;width:58px;height:21px;background:var(--purple);color:var(--white);font-size:5.2px;font-weight:600;display:flex;align-items:center;justify-content:flex-end;padding-right:12px}
.slide .brand--corner{right:20px;top:14px}

/* content slide */
.slide-title{position:absolute;left:26px;top:14px;font-size:22px;font-weight:700;color:var(--ink);letter-spacing:-.5px}
.slide-title__accent{position:absolute;left:21px;top:46px;width:32px;height:4px;border-radius:2px;background:var(--green)}
.slide-title__rule{position:absolute;left:13px;top:49px;width:562px;height:1px;background:var(--rule)}
.body-copy{position:absolute;font-size:6.9px;line-height:1.3;color:var(--text);text-align:justify}
.slide--content .body-copy{left:41px;top:95px;width:512px}
.body-copy p+p{margin-top:15px}
.body-copy p.tight{margin-top:4px}

/* section slide */
.slide--section .brand--inline{left:40px;top:111px}
.section-head{position:absolute;left:39px;top:140px;line-height:1}
.section-head__main{font-size:25px;font-weight:800;color:var(--ink)}
.section-head__sub{font-size:20.5px;font-weight:700;color:var(--purple);margin-top:3px}
.slide--section .body-copy{left:37px;top:205px;width:262px;text-align:left}
</style>
</head>
<body>
<main class="canvas">

  <section class="slide slide--title">
    <div class="bar-top"></div>
    <div class="brand brand--lg"><span class="brand__mark"></span>Quorvane</div>
    <div class="headline">
      <div class="headline__main">PRESENTATION</div>
      <div class="headline__sub">TITLE GOES HERE</div>
      <div class="headline__tagline">Sub Title Goes Here</div>
    </div>
    <div class="pill pill--presenter">Presenter Name</div>
    <div class="bar-bottom"></div>
  </section>

  <section class="slide slide--cover">
    <div class="cover-photo" role="img" aria-label="Photo of colleagues working at a table with laptops, tinted purple"></div>
    <div class="cover-text">
      <div class="cover-url">WWW.QUORVANE.EXAMPLE</div>
      <div class="cover-title">PRESENTATION</div>
      <div class="cover-subtitle">TITLE GOES HERE</div>
      <div class="cover-tagline">Sub Title Goes Here</div>
    </div>
    <div class="pill pill--date">Oct 2020</div>
    <div class="brand brand--lg"><span class="brand__mark"></span>Quorvane</div>
  </section>

  <section class="slide slide--content">
    <h1 class="slide-title">Here Goes Title Of This Slide</h1>
    <div class="slide-title__rule"></div>
    <div class="slide-title__accent"></div>
    <div class="brand brand--sm brand--corner"><span class="brand__mark"></span>Quorvane</div>
    <div class="body-copy">
      <p>Lorem ipsum dolor sit amet, consectetur adipiscing elit, sed do eiusmod tempor incididunt ut labore et dolore magna aliqua. Lorem ipsum dolor sit amet, consectetur adipiscing elit, sed do eiusmod tempor incididunt ut labore et dolore magna aliqua. Ut enim ad minim veniam, quis nostrud exercitation ullamco laboris nisi ut aliquip.</p>
      <p>Lorem ipsum dolor sit amet, consectetur adipiscing elit, Lorem ipsum dolor sit amet, consectetur adipiscing elit, sed do eiusmod tempor incididunt ut labore et dolore magna aliqua. Lorem ipsum dolor sit amet, consectetur adipiscing elit, sed do eiusmod tempor incididunt ut labore et dolore magna aliqua. Ut enim ad minim veniam, quis nostrud exercitation ullamco laboris nisi ut aliquip.</p>
      <p>Lorem ipsum dolor sit amet, consectetur adipiscing elit, sed do eiusmod tempor incididunt ut labore et dolore magna aliqua. Lorem ipsum dolor sit amet, consectetur adipiscing elit, sed do eiusmod tempor incididunt ut labore et dolore magna aliqua.</p>
      <p class="tight">sed do eiusmod tempor incididunt ut labore et dolore magna aliqua. Lorem ipsum dolor sit amet, consectetur adipiscing elit, sed do eiusmod tempor incididunt ut labore et dolore magna aliqua. Lorem ipsum dolor sit amet, consectetur adipiscing elit, sed do eiusmod tempor incididunt ut labore et dolore magna aliqua. Lorem ipsum dolor sit amet, consectetur adipiscing elit, sed do eiusmod tempor incididunt ut labore et dolore magna aliqua. Ut enim ad minim veniam, quis nostrud exercitation ullamco laboris nisi ut aliquip.</p>
      <p>Lorem ipsum dolor sit amet, consectetur adipiscing elit, sed do eiusmod tempor incididunt ut labore et dolore magna aliqua. Lorem ipsum dolor sit amet, consectetur adipiscing elit, sed do eiusmod tempor incididunt ut labore et dolore magna aliqua.</p>
    </div>
    <footer class="footer">
      <span class="footer__copy">COPYRIGHT © 2021 | ALL RIGHTS RESERVED</span>
      <span class="footer__page">PAGE | 4</span>
    </footer>
  </section>

  <section class="slide slide--section">
    <div class="brand brand--sm brand--corner"><span class="brand__mark"></span>Quorvane</div>
    <div class="brand brand--sm brand--inline"><span class="brand__mark"></span>Quorvane</div>
    <div class="section-head">
      <div class="section-head__main">SECTION HEADER</div>
      <div class="section-head__sub">Title here</div>
    </div>
    <div class="body-copy">
      <p>Lorem ipsum dolor sit amet, consectetur adipiscing elit, sed do eiusmod tempor incididunt ut labore et dolore magna aliqua. Lorem ipsum dolor sit amet, consectetur adipiscing elit, sed do eiusmod tempor incididunt ut labore et dolore magna aliqua. Ut enim ad minim veniam, quis nostrud exercitation ullamco laboris nisi ut aliquip.</p>
    </div>
    <footer class="footer">
      <span class="footer__copy">COPYRIGHT © 2021 | ALL RIGHTS RESERVED</span>
      <span class="footer__page">PAGE | 5</span>
    </footer>
  </section>

</main>
</body>
</html>
```